Land Buying Company Needs Letterhead for Direct Mail Marketing to Land Owners

We are looking for a professional letterhead that we will be including in our direct mail marketing. We will be sending this to land owners who may be interested in selling or purchasing land.

The letterhead needs to be editable. Headers and footers would look nice, but we are open. We would want it to include our address, website, phone, and email info. For right now the address to use for design purposes would the following:

Address: 415 Bramwell Avenue #600
Dallas, TX 75219
Website - www.quillridgeacres.example
Email - info@quillridgeacres.example
Phone - 866-402-ACRE

I have attached our logo zip file that we just had done on Pixel Guild. Let me know what questions you have, and thank you.

```html
<!DOCTYPE html>
<html lang="en">
<head>
<meta charset="utf-8">
<title>Quill Ridge Acres – Letterhead</title>
<link rel="stylesheet" href="https://fonts.googleapis.com/css2?family=Mulish:wght@400;700&display=swap">
<style>
  :root {
    --forest: #4a5e23;
    --leaf: #9cc31b;
    --mist: #f0f0f0;
    --paper: #ffffff;
    --ink: #1e1e1e;
  }
  * { margin: 0; padding: 0; box-sizing: border-box; }
  html, body {
    width: 849px;
    height: 1200px;
    overflow: hidden;
    background: var(--paper);
  }
  .letterhead {
    position: relative;
    width: 849px;
    height: 1200px;
    overflow: hidden;
    background: var(--paper);
    font-family: "Mulish", sans-serif;
    color: var(--ink);
  }
  .backdrop {
    position: absolute;
    inset: 0;
    width: 849px;
    height: 1200px;
  }
  .brand-panel {
    position: absolute;
    left: 518px;
    top: 0;
    width: 288px;
    height: 152px;
    background: var(--forest);
    display: flex;
    align-items: center;
    padding-left: 16px;
    padding-bottom: 28px;
    gap: 12px;
  }
  .brand-dot {
    width: 54px;
    height: 54px;
    border-radius: 50%;
    background: var(--paper);
    flex: none;
  }
  .brand-name {
    font-family: "Mulish", sans-serif;
    font-weight: 700;
    font-size: 23px;
    line-height: 1.05;
    letter-spacing: 1.5px;
    text-transform: uppercase;
    color: var(--leaf);
  }
  .contact {
    position: absolute;
    left: 0;
    width: 100%;
    text-align: center;
    font-size: 14.5px;
    font-weight: 400;
    color: var(--ink);
    white-space: nowrap;
  }
  .contact--address { top: 1138px; }
  .contact--lines { top: 1162px; }
  .contact .divider { margin: 0 12px; }
  .base-band {
    position: absolute;
    left: 0;
    bottom: 0;
    width: 100%;
    height: 13px;
    background: var(--forest);
  }
</style>
</head>
<body>
  <main class="letterhead">
    <svg class="backdrop" viewBox="0 0 849 1200" role="img" aria-label="Large pale grey sun disc with a forest of tree silhouettes and a flying bird as a faint background decoration">
      <circle cx="425" cy="682" r="576" fill="var(--mist)"/>
    </svg>

    <header class="brand-panel">
      <span class="brand-dot" aria-hidden="true"></span>
      <span class="brand-name">Quill Ridge<br>Acres</span>
    </header>

    <footer>
      <p class="contact contact--address">415 Bramwell Avenue #600 Dallas, TX 75219</p>
      <p class="contact contact--lines">866-402-ACRE<span class="divider">I</span>info@quillridgeacres.example<span class="divider">I</span>www.quillridgeacres.example</p>
      <div class="base-band"></div>
    </footer>
  </main>
</body>
</html>
```